Korelith InsurTech Website Redesign - 10 Pages

Design a modern, professional website for Korelith, an AI-native cyber insurance platform serving SMBs.

DELIVERABLE: 10 pages (desktop + mobile mockups)
- Homepage (priority #1)
- 4 Platform pages (Cyber Insurance, Brokers, Underwriters, Policyholder)
- 3 Company pages (About Us, Team, Contact/Careers)
- 2 Risk pages (AI Risk, Cyber Risk)

DESIGN DIRECTION:
- Professional + innovative (insurance meets technology)
- Trust-building + modern aesthetic
- Reference: Brambury Insurance, Tidewick Insurance
- Use official brand colors (6-color palette provided)
- Avoid generic security clipart (padlocks, shields, magnifying glasses)
- Custom graphics, not AI-generated or stock imagery

CURRENT SITES FOR REFERENCE:
- www.korelith.ai
- https://a3c9124d.korelith-website.vorlapages.dev/

Full detailed brief with all content, page specifications, and brand guidelines attached as PDF (Korelith_PixelHarbor_Brief.pdf).

TARGET AUDIENCE: Insurance brokers (primary), SMB business owners (secondary)
KEY MESSAGE: "Cyber Insurance the Way It Should Be"

Additional brand assets available in Google Drive - link provided on request.

```html
<!DOCTYPE html>
<html lang="en">
<head>
<meta charset="utf-8">
<title>Korelith — Cyber Insurance the Way It Should Be</title>
<link href="https://fonts.googleapis.com/css2?family=Montserrat:wght@500;600;700;800&family=Open+Sans:wght@400;600&display=swap" rel="stylesheet">
<style>
:root{
  --teal-900:#062c2b;
  --teal-800:#0b3d3a;
  --teal-700:#12524c;
  --teal-600:#1b6b61;
  --mint:#7be8a6;
  --mint-soft:#c9f5da;
  --ink:#10211f;
  --muted:#5d6b69;
  --line:#d9e2e0;
  --paper:#ffffff;
  --mist:#eef3f6;
  --tan-1:#cdb890;
  --tan-2:#b39a6c;
  --tan-3:#97805a;
  --sand:#f4ede0;
}
*{box-sizing:border-box;margin:0;padding:0}
html,body{width:1200px;height:3796px;overflow:hidden}
body{font-family:"Open Sans",Arial,sans-serif;color:var(--ink);background:var(--paper)}
h1,h2,h3,h4,.brand,.btn,.tab,.ticker span{font-family:"Montserrat",Arial,sans-serif}
section,header,footer{position:relative;width:1200px;overflow:hidden}

/* Header + hero */
.hero{height:640px;background:radial-gradient(circle at 75% 40%,var(--teal-600),var(--teal-800) 45%,var(--teal-900));color:#fff}
.nav{display:flex;align-items:center;justify-content:space-between;padding:22px 40px;position:relative;z-index:2}
.brand{display:flex;align-items:center;gap:8px;font-weight:700;font-size:15px;color:#fff}
.brand-dot{width:26px;height:26px;border-radius:50%;background:var(--mint)}
.nav-links{display:flex;align-items:center;gap:26px;font-family:"Montserrat",sans-serif;font-size:13px;font-weight:600}
.btn{display:inline-block;font-weight:700;font-size:12px;border-radius:4px;padding:9px 16px}
.btn-outline{border:1px solid #fff;color:#fff}
.btn-mint{background:var(--mint);color:var(--teal-900)}
.hero-visual{position:absolute;right:0;top:0;width:760px;height:640px;background:radial-gradient(ellipse at 60% 55%,rgba(123,232,166,.25),rgba(6,44,43,0) 65%)}
.hero-copy{position:absolute;left:40px;top:360px;width:520px;z-index:2}
.hero-copy h1{font-size:44px;line-height:1.15;font-weight:700}
.hero-copy p{font-size:13px;margin:12px 0 20px;opacity:.85}

/* Ticker */
.ticker{height:32px;background:var(--mint);display:flex;align-items:center;justify-content:space-around;white-space:nowrap}
.ticker span{font-weight:700;font-size:13px;color:var(--teal-900)}

/* Different */
.different{height:528px;text-align:center;padding-top:66px}
.section-title{font-size:30px;font-weight:700;color:var(--ink)}
.section-lead{font-size:12px;color:var(--muted);width:560px;margin:10px auto 0;line-height:1.6}
.hub{width:64px;height:64px;border-radius:50%;background:var(--teal-800);margin:26px auto 0;display:flex;align-items:center;justify-content:center;color:#fff;font-size:10px;font-weight:700;font-family:"Montserrat",sans-serif;position:relative;z-index:2}
.connector{position:absolute;left:0;top:230px}
.cards{display:flex;gap:20px;justify-content:center;margin-top:30px}
.card{width:170px;height:232px;background:#fff;border:1px solid var(--line);border-radius:8px;box-shadow:0 6px 18px rgba(10,50,45,.08);padding:22px 14px}
.card-icon{width:42px;height:42px;border-radius:50%;background:var(--mint-soft);margin:0 auto 14px;display:flex;align-items:center;justify-content:center}
.card h3{font-size:13px;font-weight:700;line-height:1.35}
.card p{font-size:10px;color:var(--muted);margin-top:10px;line-height:1.55}

/* Tools */
.tools{height:400px;background:var(--mist);display:flex;align-items:center;gap:40px;padding:0 110px}
.dashboard{width:470px;height:300px;border-radius:8px;background:linear-gradient(135deg,#ffffff,#dde7ea);box-shadow:0 8px 24px rgba(10,50,45,.12)}
.tools-copy{width:440px;background:#fff;border-radius:8px;padding:30px 32px;box-shadow:0 8px 24px rgba(10,50,45,.08)}
.tools-copy h2{font-size:28px;line-height:1.2;font-weight:700}
.tools-copy p{font-size:11px;color:var(--muted);margin:10px 0 14px;line-height:1.6}
.ticks li{list-style:none;display:flex;gap:8px;align-items:center;font-size:11.5px;margin-bottom:8px}

/* Faint wordmark */
.faint{height:120px;display:flex;align-items:center;justify-content:center;font-family:"Montserrat",sans-serif;font-size:92px;font-weight:800;color:#eef1f2;letter-spacing:2px;white-space:nowrap}
.faint.short{height:100px}

/* DNA */
.dna{height:440px;text-align:center;padding-top:40px}
.dna-row{display:flex;justify-content:center;gap:46px;margin-top:40px}
.dna-item{width:220px;height:220px;border-radius:50%;display:flex;align-items:center;justify-content:center;padding:34px;color:#fff;font-family:"Montserrat",sans-serif;font-weight:700;font-size:15px;line-height:1.35;border:6px solid var(--mint-soft)}
.dna-item.solid{background:var(--teal-800)}
.dna-item.photo{background:radial-gradient(circle at 40% 35%,var(--teal-600),var(--teal-900))}

/* Lifecycle */
.lifecycle{height:548px;background:linear-gradient(180deg,#fff 0%,var(--sand) 35%,var(--sand) 100%);text-align:center;padding-top:70px}
.houses{position:absolute;left:215px;bottom:70px;display:flex;align-items:flex-end;gap:10px}
.house{width:146px;color:#fff;text-align:left;padding:0 14px 18px;clip-path:polygon(0 40px,50% 0,100% 40px,100% 100%,0 100%);display:flex;flex-direction:column;justify-content:flex-end}
.house .ico{width:30px;height:30px;border-radius:50%;background:rgba(255,255,255,.9);margin-bottom:10px;display:flex;align-items:center;justify-content:center}
.house h4{font-size:14px;font-weight:700}
.house p{font-size:9.5px;line-height:1.5;margin-top:4px;opacity:.95}
.h1{height:230px;background:var(--tan-3)}
.h2{height:262px;background:var(--tan-1)}
.h3{height:294px;background:var(--tan-3)}
.h4{height:326px;background:var(--tan-1)}
.h5{height:358px;background:var(--tan-2)}

/* Integrations */
.integrations{height:300px;text-align:center;padding-top:30px}
.tabs{display:flex;justify-content:center;gap:8px;margin-top:22px}
.tab{font-size:11px;font-weight:600;padding:9px 20px;border-radius:4px;background:var(--mist);color:var(--muted)}
.tab.active{background:var(--mint);color:var(--teal-900)}
.partners{display:flex;justify-content:center;gap:22px;margin-top:34px}
.partner{width:160px;height:70px;border:1px solid var(--line);border-radius:6px;display:flex;align-items:center;justify-content:center;font-family:"Open Sans",sans-serif;font-weight:600;font-size:15px;color:var(--ink);box-shadow:0 4px 12px rgba(10,50,45,.06)}

/* CTA */
.cta{height:380px;background:linear-gradient(180deg,var(--teal-700),var(--teal-800))}
.cta-card{position:absolute;left:40px;top:60px;width:1120px;height:260px;border-radius:10px;background:linear-gradient(110deg,var(--teal-600),#3d9b86 70%,#7fd0b0);padding:60px 56px;color:#fff}
.cta-card h2{font-size:38px;font-weight:700}
.cta-card p{font-size:11.5px;width:420px;line-height:1.6;margin:12px 0 22px;opacity:.9}
.cta-card .btn{background:#fff;color:var(--teal-900)}
.cta-person{position:absolute;right:110px;top:20px;width:320px;height:300px;border-radius:10px 10px 0 0;background:linear-gradient(180deg,rgba(255,255,255,.25),rgba(255,255,255,.05))}

/* Footer */
.footer{height:276px;background:var(--teal-900);color:#d9ece6;padding:44px 40px 0}
.footer-grid{display:flex;gap:60px}
.footer-about{width:260px;font-size:10.5px;line-height:1.6}
.footer-about .brand{margin-bottom:12px}
.footer-col h4{font-size:13px;font-weight:700;color:#fff;margin-bottom:12px}
.footer-col li{list-style:none;font-size:11px;margin-bottom:8px}
.social li{display:flex;align-items:center;gap:8px}
.social i{width:18px;height:18px;border-radius:50%;background:var(--teal-700);display:inline-block}
.newsletter p{font-size:10.5px;width:220px;line-height:1.5;margin-bottom:10px}
.sub{display:flex;width:240px;background:#fff;border-radius:4px;padding:4px}
.sub span{flex:1;font-size:10px;color:var(--muted);padding:7px 8px}
.copyright{position:absolute;left:0;bottom:16px;width:100%;text-align:center;font-size:10px;color:#8fb3aa;border-top:1px solid var(--teal-700);padding-top:12px}
</style>
</head>
<body>

<header class="hero">
  <nav class="nav">
    <div class="brand"><span class="brand-dot"></span>Korelith</div>
    <div class="nav-links">
      <span>Platform ▾</span><span>Resources</span><span>Company ▾</span>
      <span class="btn btn-outline">Get a Demo</span>
    </div>
  </nav>
  <div class="hero-visual" role="img" aria-label="Abstract peak graphic with a professional working at a laptop"></div>
  <div class="hero-copy">
    <h1>Cyber Insurance the<br>Way It Should Be</h1>
    <p>Evidence-based, automation-driven underwriting for the AI era</p>
    <span class="btn btn-mint">Contact Us</span>
  </div>
</header>

<div class="ticker">
  <span>Korelith</span><span>Korelith</span><span>Korelith</span><span>Korelith</span><span>Korelith</span><span>Korelith</span><span>Korelith</span><span>Korelith</span><span>Korelith</span>
</div>

<section class="different">
  <h2 class="section-title">What Makes Korelith Different</h2>
  <p class="section-lead">The Korelith platform streamlines the entire policy lifecycle, from quote to renewal, giving brokers and underwriters real-time clarity into cyber risk.</p>
  <svg class="connector" width="1200" height="80" viewBox="0 0 1200 80" fill="none" stroke="#b9cbc7" stroke-width="1.5">
    <path d="M600 20V50M198 50H1002M198 50V80M399 50V80M600 50V80M801 50V80M1002 50V80"/>
  </svg>
  <div class="hub">Korelith</div>
  <div class="cards">
    <div class="card"><div class="card-icon"><svg width="20" height="20" viewBox="0 0 20 20" fill="none" stroke="#12524c" stroke-width="2"><rect x="3" y="4" width="14" height="11" rx="2"/></svg></div><h3>Platform-driven Assessment</h3><p>Comprehensive risk scoring built directly into the broker workflow.</p></div>
    <div class="card"><div class="card-icon"><svg width="20" height="20" viewBox="0 0 20 20" fill="none" stroke="#12524c" stroke-width="2"><path d="M4 15V9M10 15V5M16 15V11"/></svg></div><h3>Automated Analysis of Cyber Risk Data</h3><p>Continuous scans that turn raw security data into clear insights.</p></div>
    <div class="card"><div class="card-icon"><svg width="20" height="20" viewBox="0 0 20 20" fill="none" stroke="#12524c" stroke-width="2"><circle cx="10" cy="10" r="6"/><path d="M10 4V16"/></svg></div><h3>Inside-Out &amp; Outside-In Data Integrations</h3><p>Combines internal telemetry with external threat intelligence feeds.</p></div>
    <div class="card"><div class="card-icon"><svg width="20" height="20" viewBox="0 0 20 20" fill="none" stroke="#12524c" stroke-width="2"><path d="M3 14L8 9L11 12L17 6"/></svg></div><h3>AI Analysis for Risk Prediction</h3><p>Models forecast likely incidents and guide smarter pricing decisions.</p></div>
    <div class="card"><div class="card-icon"><svg width="20" height="20" viewBox="0 0 20 20" fill="none" stroke="#12524c" stroke-width="2"><circle cx="10" cy="10" r="6"/><path d="M10 6V10L13 12"/></svg></div><h3>Continuous Risk Monitoring</h3><p>Alerts policyholders early so threats are fixed before losses occur.</p></div>
  </div>
</section>

<section class="tools">
  <div class="dashboard" role="img" aria-label="Screenshot of the Korelith risk assessment dashboard"></div>
  <div class="tools-copy">
    <h2>Proprietary Tools<br>and Rapid Response</h2>
    <p>Advanced security tools and 24/7 incident response capabilities protect businesses before, during and after cyber events.</p>
    <ul class="ticks">
      <li><svg width="14" height="14" viewBox="0 0 14 14"><circle cx="7" cy="7" r="7" fill="#7be8a6"/><path d="M4 7L6 9L10 5" stroke="#062c2b" stroke-width="1.6" fill="none"/></svg>In-house ransomware response &amp; system restoration</li>
      <li><svg width="14" height="14" viewBox="0 0 14 14"><circle cx="7" cy="7" r="7" fill="#7be8a6"/><path d="M4 7L6 9L10 5" stroke="#062c2b" stroke-width="1.6" fill="none"/></svg>50+ in-house and certified expert contractors</li>
      <li><svg width="14" height="14" viewBox="0 0 14 14"><circle cx="7" cy="7" r="7" fill="#7be8a6"/><path d="M4 7L6 9L10 5" stroke="#062c2b" stroke-width="1.6" fill="none"/></svg>24/7 claims hotline with expert cyber triage</li>
      <li><svg width="14" height="14" viewBox="0 0 14 14"><circle cx="7" cy="7" r="7" fill="#7be8a6"/><path d="M4 7L6 9L10 5" stroke="#062c2b" stroke-width="1.6" fill="none"/></svg>All-ready on-site and remote support</li>
      <li><svg width="14" height="14" viewBox="0 0 14 14"><circle cx="7" cy="7" r="7" fill="#7be8a6"/><path d="M4 7L6 9L10 5" stroke="#062c2b" stroke-width="1.6" fill="none"/></svg>Real-time incident tracking</li>
    </ul>
  </div>
</section>

<div class="faint">Korelith InsurTech</div>

<section class="dna">
  <h2 class="section-title">Insurance DNA and Tech Execution</h2>
  <p class="section-lead">Founded by a team with deep expertise in cyber insurance and cybersecurity, we understand both the risk landscape and the insurance market.</p>
  <div class="dna-row">
    <div class="dna-item solid">20+ years Combined Insurance Experience</div>
    <div class="dna-item photo" role="img" aria-label="Cybersecurity team background">Cybersecurity expertise from industry leaders</div>
    <div class="dna-item photo" role="img" aria-label="Executive team background">Former executives from Emberwall, Corvane, Halden XL</div>
    <div class="dna-item photo" role="img" aria-label="Technology background">Built to address first-wave InsurTech shortcomings</div>
  </div>
</section>

<div class="ticker">
  <span>Korelith</span><span>Korelith</span><span>Korelith</span><span>Korelith</span><span>Korelith</span><span>Korelith</span><span>Korelith</span><span>Korelith</span><span>Korelith</span>
</div>

<section class="lifecycle">
  <h2 class="section-title">The Complete Cyber Insurance Lifecycle</h2>
  <div class="houses">
    <div class="house h1"><div class="ico"><svg width="14" height="14" viewBox="0 0 14 14" fill="none" stroke="#97805a" stroke-width="2"><path d="M3 7L6 10L11 4"/></svg></div><h4>Ensure</h4><p>Bind in days with clear coverage and fair pricing.</p></div>
    <div class="house h2"><div class="ico"><svg width="14" height="14" viewBox="0 0 14 14" fill="none" stroke="#97805a" stroke-width="2"><circle cx="7" cy="7" r="4"/></svg></div><h4>Assess</h4><p>Automated scans reveal exposure across every system.</p></div>
    <div class="house h3"><div class="ico"><svg width="14" height="14" viewBox="0 0 14 14" fill="none" stroke="#97805a" stroke-width="2"><path d="M3 10L7 5L11 10"/></svg></div><h4>Improve</h4><p>Actionable guidance helps clients strengthen security posture.</p></div>
    <div class="house h4"><div class="ico"><svg width="14" height="14" viewBox="0 0 14 14" fill="none" stroke="#97805a" stroke-width="2"><path d="M3 7H11M7 3V11"/></svg></div><h4>Remediate</h4><p>Expert responders restore operations quickly after incidents.</p></div>
    <div class="house h5"><div class="ico"><svg width="14" height="14" viewBox="0 0 14 14" fill="none" stroke="#97805a" stroke-width="2"><path d="M11 5A4 4 0 1 0 11 9M11 2V5H8"/></svg></div><h4>Renew</h4><p>Seamless renewals priced on demonstrated risk improvement.</p></div>
  </div>
</section>

<section class="integrations">
  <h2 class="section-title">Seamlessly Integrates With Your Tech Stack</h2>
  <div class="tabs">
    <span class="tab active">Identity Platforms</span><span class="tab">Endpoint Security</span><span class="tab">Developer Platforms</span><span class="tab">Cloud Infrastructure</span>
  </div>
  <div class="partners">
    <div class="partner">Verdane Workspace</div>
    <div class="partner">Quorra</div>
    <div class="partner">Skyvale Directory</div>
  </div>
</section>

<div class="faint short">Korelith InsurTech</div>

<section class="cta">
  <div class="cta-card">
    <h2>Let's Secure Your Future.</h2>
    <p>Get cyber coverage built on evidence, not guesswork. Talk to our team about protection that adapts as your business and its risks grow.</p>
    <span class="btn">Get started →</span>
  </div>
  <div class="cta-person" role="img" aria-label="Smiling professional holding a tablet showing a risk report"></div>
</section>

<footer class="footer">
  <div class="footer-grid">
    <div class="footer-about">
      <div class="brand"><span class="brand-dot"></span>Korelith</div>
      Protecting the finances and security of SMBs with an AI-native cyber insurance platform built for brokers.
    </div>
    <div class="footer-col"><h4>Solutions</h4><ul><li>Cyber Insurance</li><li>For Brokers</li><li>For Underwriters</li></ul></div>
    <div class="footer-col"><h4>Main Links</h4><ul><li>Platform</li><li>Resources</li><li>Company</li></ul></div>
    <div class="footer-col social"><h4>Follow Us</h4><ul><li><i></i>Friendwall</li><li><i></i>Chirpline</li><li><i></i>Linkfold</li><li><i></i>Picnest</li></ul></div>
    <div class="footer-col newsletter"><h4>Subscribe Newsletter</h4><p>Get the latest cyber risk insights delivered to your inbox.</p><div class="sub"><span>Enter your email</span><span class="btn btn-mint">Subscribe</span></div></div>
  </div>
  <div class="copyright">Copyright © 2024 Korelith. All Rights Reserved.</div>
</footer>

</body>
</html>
```